Need to create a website for a luxury custom home builder in Phoenix USA. Looking forward for some creative designs including a full page video intro on homepage and should show up pretty luxurious.

```html
<!DOCTYPE html>
<html lang="en">
<head>
<meta charset="utf-8">
<title>Crestline Homes — Custom Home Builder</title>
<link href="https://fonts.googleapis.com/css2?family=Montserrat:wght@400;600;700;800&family=Open+Sans:wght@400;600&family=Libre+Baskerville:ital@1&display=swap" rel="stylesheet">
<style>
:root{
  --blue:#1d8fd6;
  --blue-dark:#1478b8;
  --navy:#14304a;
  --green:#0b3a2c;
  --green-mid:#154f3c;
  --ink:#2b3440;
  --muted:#6b7480;
  --paper:#ffffff;
  --mist:#eef0f2;
  --line:#d9dde2;
}
*{box-sizing:border-box;margin:0;padding:0}
html,body{width:1200px;height:5376px;overflow:hidden}
body{position:relative;background:var(--paper);font-family:"Open Sans",Arial,sans-serif;color:var(--ink)}
.abs{position:absolute}
.photo{position:absolute}
h1,h2,h3,.btn,.nav,.eyebrow{font-family:"Montserrat",Arial,sans-serif}
.btn{display:inline-block;background:var(--navy);color:#fff;font-size:13px;font-weight:700;letter-spacing:1px;padding:10px 20px;text-transform:uppercase}
.btn.blue{background:var(--blue)}
.btn.outline{background:#fff;color:var(--blue);border:2px solid var(--blue)}
.brand{font-family:"Montserrat",Arial,sans-serif;font-weight:800;color:#fff;font-size:26px;letter-spacing:2px;text-align:center;display:flex;align-items:center;gap:10px}
.brand i{display:inline-block;width:16px;height:16px;border-radius:50%;background:#fff}
.ghost-word{position:absolute;font-family:"Montserrat",Arial,sans-serif;font-weight:800;font-size:120px;letter-spacing:6px;color:transparent;-webkit-text-stroke:2px rgba(20,48,74,.12);transform:rotate(-90deg);transform-origin:left top;white-space:nowrap}
/* header */
.hero-photo{left:0;top:0;width:1200px;height:560px;background:linear-gradient(180deg,#2a2d5c 0%,#5b4b7a 40%,#c98c6a 70%,#2a3a2a 100%)}
.nav{top:34px;font-size:12px;font-weight:700;color:#fff;letter-spacing:1px}
.nav-left{left:30px;display:flex;gap:22px}
.nav-right{right:30px;display:flex;gap:16px;align-items:center}
.menu-btn{width:38px;height:38px;border-radius:50%;background:var(--blue);display:flex;align-items:center;justify-content:center}
.hero-box{left:0;top:468px;width:840px;height:204px;background:var(--blue);padding:28px 120px;color:#fff}
.crumbs{font-size:11px;letter-spacing:1px;opacity:.85;margin-bottom:14px}
.hero-box h1{font-size:34px;font-weight:700;letter-spacing:1px;margin-bottom:18px}
/* plans */
.plan-card{left:120px;top:740px;width:440px;height:500px;background:#fff;box-shadow:0 10px 40px rgba(0,0,0,.12);padding:40px 44px;z-index:2}
.plan-card h2{font-size:32px;line-height:1.1;color:var(--blue);font-weight:700;margin-bottom:20px}
.plan-card li{font-size:13px;line-height:1.5;margin:0 0 10px 16px}
.plan-card p{font-size:13px;line-height:1.6;color:var(--muted);margin:14px 0 20px}
.link{font-family:"Montserrat",Arial,sans-serif;font-size:12px;font-weight:700;color:var(--blue);letter-spacing:1px;border-bottom:2px solid var(--blue);padding-bottom:4px}
/* approach */
.approach{left:0;top:1600px;width:1200px;height:300px;background:linear-gradient(100deg,#0a3328,#1a5a44 50%,#0c3a2d)}
.approach h3{position:absolute;left:425px;top:140px;color:#fff;font-size:30px;font-weight:600;letter-spacing:2px}
.approach p{position:absolute;left:720px;top:120px;width:300px;color:#e6f0ec;font-size:14px;line-height:1.5}
/* plan step */
.step-bg{left:0;top:1900px;width:1200px;height:380px;background:var(--mist)}
.step-panel{left:480px;top:1920px;width:720px;height:360px;background:var(--blue);padding:110px 70px;color:#fff}
.step-panel h3{font-size:30px;font-weight:600;margin-bottom:18px}
.step-panel p{font-size:14px;line-height:1.6;width:420px;margin-bottom:28px;opacity:.9}
/* projects */
.section-title{font-size:30px;font-weight:700;color:var(--blue);letter-spacing:1px}
.proj{top:2390px;width:300px}
.proj .photo{position:relative;height:230px}
.proj .meta{font-size:10px;color:var(--muted);letter-spacing:1px;margin-top:14px;text-transform:uppercase}
.proj .name{font-family:"Montserrat",Arial,sans-serif;font-size:13px;color:var(--blue);font-weight:600;margin-top:4px;text-transform:uppercase}
.arrows{display:flex;gap:10px;align-items:center;color:var(--blue);font-size:22px;font-weight:700}
/* dream */
.dream{left:0;top:2760px;width:1200px;height:1320px;background:var(--green)}
.dream-card{left:580px;top:2810px;width:420px;height:390px;background:#fff;padding:44px 44px;z-index:2}
.dream-card h2{font-size:38px;color:var(--blue);font-weight:700;line-height:1.1;margin-bottom:20px}
.dream-card p{font-size:12.5px;line-height:1.6;color:var(--muted);margin-bottom:12px}
.quote{left:90px;top:3720px;width:450px;height:280px;background:#fff;padding:40px;z-index:2}
.quote blockquote{font-family:"Libre Baskerville",Georgia,serif;font-style:italic;font-size:20px;line-height:1.5;color:var(--ink)}
.quote cite{display:block;font-family:"Libre Baskerville",Georgia,serif;font-size:12px;margin-top:18px;color:var(--muted)}
/* services */
.services{left:0;top:4080px;width:1200px;height:900px;background:var(--mist)}
.svc{position:absolute;background:#fff}
.svc .label{position:absolute;left:0;top:0;background:#fff;font-family:"Montserrat",Arial,sans-serif;font-size:15px;font-weight:600;color:var(--ink);padding:10px 16px;z-index:2}
.svc .go{position:absolute;right:14px;bottom:14px;width:30px;height:30px;border-radius:50%;background:#fff;display:flex;align-items:center;justify-content:center}
/* partners & footer */
.partners{left:0;top:4980px;width:1200px;height:110px;background:#10191f;display:flex;align-items:center;justify-content:center;gap:50px}
.partners span{font-family:"Montserrat",Arial,sans-serif;color:#c9d0d6;font-size:12px;letter-spacing:2px;font-weight:600}
.badge{width:90px;height:44px;background:#3a444c;border-radius:3px}
.footer{left:0;top:5090px;width:1200px;height:230px;background:var(--blue);color:#fff}
.footer-links{position:absolute;left:235px;top:90px;display:flex;gap:22px;font-family:"Montserrat",Arial,sans-serif;font-size:13px;font-weight:600}
.footer-contact{position:absolute;right:60px;top:60px;text-align:right;font-size:12px;line-height:1.6}
.legal{left:0;top:5320px;width:1200px;height:56px;background:#fff;display:flex;gap:20px;align-items:center;padding-left:40px;font-size:10px;color:var(--muted)}
</style>
</head>
<body>

<!-- Hero -->
<div class="photo hero-photo" role="img" aria-label="Modern two-storey luxury home lit warmly at dusk"></div>
<nav class="abs nav nav-left"><span>ABOUT</span><span>SERVICES</span><span>PROCESS</span><span>PROJECTS</span></nav>
<div class="abs" style="left:0;width:1200px;top:22px;display:flex;justify-content:center"><div class="brand"><i></i>CRESTLINE HOMES</div></div>
<div class="abs nav nav-right"><span>CONTACT</span><span class="menu-btn"><svg width="16" height="12"><rect width="16" height="2" fill="#fff"/><rect y="5" width="16" height="2" fill="#fff"/><rect y="10" width="16" height="2" fill="#fff"/></svg></span></div>
<section class="abs hero-box">
  <div class="crumbs">HOME &nbsp;›&nbsp; SERVICES &nbsp;›&nbsp; CUSTOM HOMES</div>
  <h1>INSPIRED CUSTOM HOMES START HERE</h1>
  <span class="btn">Where we build →</span>
</section>

<!-- Plans -->
<section class="abs plan-card">
  <h2>OUR CUSTOM HOME PLANS,YOUR VISION</h2>
  <ul>
    <li>Want a home personalized to your family?</li>
    <li>Need help balancing your wish list with your budget?</li>
    <li>Thinking about building your own custom home but don't know where to start?</li>
  </ul>
  <p>There are many steps and decisions to make when building a custom home. It's important to work with a company you trust to navigate the process. You're busy with work and family life; you don't have the time or experience to manage your own construction project. Having a single point of contact makes it easy, and keeps your project on schedule and on budget.</p>
  <span class="link">LEARN ABOUT OUR PROCESS →</span>
</section>
<div class="photo" style="left:600px;top:720px;width:400px;height:360px;background:linear-gradient(160deg,#dfe3e6,#6d7177 60%,#3a3d42)" role="img" aria-label="Contemporary black and white cube-shaped house in daylight"></div>
<div class="photo" style="left:80px;top:1110px;width:860px;height:440px;background:linear-gradient(180deg,#0e1e3a,#2c3d5c 55%,#d9c39a 80%,#3a4a3a)" role="img" aria-label="Modern white villa illuminated at night, video preview"></div>
<svg class="abs" style="left:490px;top:1300px" width="60" height="60" viewBox="0 0 60 60"><circle cx="30" cy="30" r="29" fill="#fff"/><path d="M24 19 L42 30 L24 41Z" fill="#14304a"/></svg>

<!-- Approach -->
<section class="abs approach" role="img" aria-label="Dark green tinted photo of a house under construction">
  <div class="ghost-word" style="left:130px;top:290px;font-size:110px;-webkit-text-stroke:2px rgba(255,255,255,.18)">PROCESS</div>
  <h3>APPROACH</h3>
  <p>"Custom" doesn't automatically mean "expensive." It means your ideas, within your price range, are applied to fit your specific needs. Work with us to design and build your dream home within your budget and ideal location.</p>
</section>

<!-- Plan step -->
<div class="abs step-bg"></div>
<section class="abs step-panel">
  <h3>2. Plan</h3>
  <p>Whether you already have a plan or need to create one, it is a collaborative process to ensure that your plan fits your needs and budget.</p>
  <span class="btn">Discover more →</span>
</section>

<!-- Projects -->
<div class="ghost-word" style="left:60px;top:2720px">INSPIRE</div>
<h2 class="abs section-title" style="left:265px;top:2312px">CUSTOM HOME PROJECTS</h2>
<span class="abs btn outline" style="left:720px;top:2312px">All projects →</span>
<article class="abs proj" style="left:265px"><div class="photo" style="background:linear-gradient(170deg,#5c6c80,#b0906a 60%,#2b2b2b)" role="img" aria-label="Modern home with dark wood cladding at sunset"></div><div class="meta">Custom Home</div><div class="name">Villa Estate by the City</div></article>
<article class="abs proj" style="left:580px"><div class="photo" style="background:linear-gradient(180deg,#7fb2d8,#e8e4dc 55%,#2f86c8)" role="img" aria-label="White modern home with blue pool"></div><div class="meta">Custom Home</div><div class="name">Desert Villa</div></article>
<article class="abs proj" style="left:890px"><div class="photo" style="background:linear-gradient(180deg,#e9eef2,#8da5b8 60%,#3d4d5a)" role="img" aria-label="Bright open-plan living room interior"></div><div class="meta">Custom Home</div><div class="name">Canyon Lookout</div></article>
<div class="abs arrows" style="left:265px;top:2690px"><span>←</span><span>→</span></div>

<!-- Dream -->
<div class="abs dream"></div>
<section class="abs dream-card">
  <h2>BUILD YOUR DREAM HOME.</h2>
  <p>Let's work together to design a beautiful and functional home completely customized to you. We can help you no matter where you are in the custom home building process. Reach out to discuss your unique scenario.</p>
  <p>With decades of custom home building experience and a commitment to excellence and innovation in home designs, there is no better way to experience the highest home difference than to explore one of our custom built model homes.</p>
  <span class="btn" style="margin-top:6px">Find a model home →</span>
</section>
<div class="photo" style="left:120px;top:3040px;width:300px;height:320px;background:linear-gradient(180deg,#f2f1ee,#c9c3b8 60%,#8e877c)" role="img" aria-label="Light living room interior with sofa"></div>
<div class="photo" style="left:400px;top:3220px;width:600px;height:380px;background:linear-gradient(170deg,#d8dde2,#5f6870 55%,#262a2e)" role="img" aria-label="Glass-walled modern house exterior"></div>
<div class="photo" style="left:450px;top:3720px;width:660px;height:320px;background:linear-gradient(180deg,#e8e2d8,#c8b49a 60%,#5a6f86)" role="img" aria-label="Family sitting together in their new home"></div>
<section class="abs quote">
  <blockquote>Ridgeview Homes allowed my wife and I to fulfill our dreams. It has been almost three years since we finished our project, and we still pinch ourselves every day.</blockquote>
  <cite>-Daniel, Homeowner</cite>
</section>
<div class="abs arrows" style="left:130px;top:4030px;color:#fff;font-size:18px"><span>←</span><span>→</span></div>

<!-- Services -->
<div class="abs services"></div>
<div class="ghost-word" style="left:60px;top:4560px">DESIGN</div>
<div class="ghost-word" style="left:1060px;top:4880px;font-size:100px">BUILD</div>
<h2 class="abs section-title" style="left:265px;top:4248px">OTHER SERVICES</h2>
<div class="svc" style="left:360px;top:4330px;width:340px;height:270px;background:linear-gradient(180deg,#dfe4e8,#9aa7b3 60%,#4a5560)" role="img" aria-label="White modern kitchen"><span class="label">Kitchen Remodels</span></div>
<div class="svc" style="left:740px;top:4330px;width:340px;height:270px;background:linear-gradient(180deg,#d5d9de,#3d95c7 60%,#1b5a7e)" role="img" aria-label="Bathroom with blue vanity"><span class="label">Bathroom Remodels</span></div>
<div class="svc" style="left:80px;top:4540px;width:360px;height:320px;background:linear-gradient(180deg,#c8ccd4,#4a5168 60%,#1e2233)" role="img" aria-label="Whole house interior renovation"><span class="label">Whole House<br>Remodels</span><span class="go"><svg width="12" height="12"><path d="M3 6h7M7 3l3 3-3 3" stroke="#14304a" stroke-width="2" fill="none"/></svg></span></div>
<div class="svc" style="left:480px;top:4600px;width:400px;height:300px;background:linear-gradient(180deg,#e4e6ea,#7c8ba8 60%,#2e3a55)" role="img" aria-label="New home addition living space"><span class="label">Home Additions</span><span class="go"><svg width="12" height="12"><path d="M3 6h7M7 3l3 3-3 3" stroke="#14304a" stroke-width="2" fill="none"/></svg></span></div>

<!-- Partners -->
<section class="abs partners">
  <span>OUR PARTNERS</span>
  <div class="badge"></div><div class="badge"></div><div class="badge"></div><div class="badge"></div>
</section>

<!-- Footer -->
<footer class="abs footer">
  <div class="abs" style="left:0;width:1200px;top:50px;display:flex;justify-content:center"><div class="brand"><i></i>CRESTLINE HOMES</div></div>
  <div class="footer-links"><span>Login</span><span>FAQs</span><span>Reviews</span><span>Events</span><span>Press</span></div>
  <span class="abs btn" style="left:235px;top:150px">Get a free estimate</span>
  <div class="footer-contact">125 Mesa Ridge Road<br>Phoenix, AZ 85000<br><br>Phone: 555-0142<br>Monday – Friday 8am – 5pm</div>
</footer>
<div class="abs legal"><span>©2024 Crestline Homes</span><span>Terms &amp; Conditions</span><span>Sitemap</span><span>Privacy Policy</span></div>

</body>
</html>
```